Design new marketing postcard for mortgage loan applicants

I have provided a postcard recently designed as a possible guide for this project and have attached it. The new text is rough drafted and included. Please feel free to design outside of the old postcard or you can design close to it.

```html
<!DOCTYPE html>
<html lang="en">
<head>
<meta charset="utf-8">
<title>Cash Out Equity Loan Postcard</title>
<link rel="stylesheet" href="https://fonts.googleapis.com/css2?family=Oswald:wght@600;700&family=PT+Sans:wght@400;700&display=swap">
<style>
  :root {
    --navy: #0f3558;
    --navy-deep: #0b2a48;
    --red: #e31e24;
    --red-deep: #b0111a;
    --gold: #f3c97a;
    --gold-ring: #c98a3a;
    --silver: #d3cfd2;
    --paper: #ffffff;
    --backdrop: #6e6e6e;
    --ink: #1c2a3a;
    --rule: #c9c9c9;
    --stamp: #dcdcdc;
  }
  * { margin: 0; padding: 0; box-sizing: border-box; }
  html, body { width: 1200px; height: 1200px; overflow: hidden; }
  body { background: var(--backdrop); position: relative; font-family: "PT Sans", sans-serif; }

  .card { position: absolute; left: 217px; width: 766px; height: 520px; background: var(--paper); overflow: hidden; }
  .card--front { top: 42px; }
  .card--back { top: 626px; }

  /* front */
  .photo {
    position: absolute; left: 375px; top: 104px; width: 391px; height: 416px;
    background: linear-gradient(90deg, rgba(255,255,255,1) 0%, rgba(236,214,196,0.7) 25%, #d9bfa8 45%, #cfd9c8 80%, #8fae6a 100%);
  }
  .headline {
    position: absolute; left: 36px; top: 45px;
    font-family: "Oswald", sans-serif; font-weight: 700; color: var(--red);
    font-size: 67px; line-height: 62px; letter-spacing: 0.5px; text-transform: uppercase;
  }
  .subhead-bar {
    position: absolute; left: 35px; top: 190px; width: 351px; height: 33px;
    background: var(--navy); color: #fff; font-size: 23px; line-height: 33px; text-align: center;
  }
  .benefits-title {
    position: absolute; left: 37px; top: 259px;
    color: var(--navy); font-weight: 700; font-size: 19px; line-height: 22px; letter-spacing: 0.2px;
  }
  .benefits { position: absolute; left: 47px; top: 294px; list-style: none; }
  .benefits li { display: flex; align-items: center; gap: 10px; font-size: 16px; color: var(--ink); height: 24px; }
  .benefits svg { width: 16px; height: 16px; }

  .brand { position: absolute; display: flex; align-items: center; gap: 10px; color: var(--navy); font-weight: 700; }
  .brand__dot { width: 30px; height: 30px; border-radius: 50%; background: var(--gold-ring); flex: none; }
  .brand--front { left: 503px; top: 34px; font-size: 18px; line-height: 1.1; }
  .nmls { position: absolute; left: 604px; top: 97px; font-size: 16px; color: var(--ink); }

  .call-band { position: absolute; left: 0; bottom: 0; width: 460px; height: 102px; }
  .call {
    position: absolute; display: flex; align-items: center; gap: 20px;
    font-family: "Oswald", sans-serif; font-weight: 600; color: var(--gold); font-size: 44px; line-height: 1; letter-spacing: 0.5px;
  }
  .call__icon { width: 64px; height: 64px; border-radius: 50%; background: var(--gold); display: flex; align-items: center; justify-content: center; }
  .call__icon svg { width: 34px; height: 34px; }
  .call--front { left: 24px; top: 438px; }

  /* back */
  .back-shape { position: absolute; left: 0; top: 0; width: 766px; height: 520px; }
  .message p { position: absolute; left: 21px; color: #fff; }
  .message__intro { top: 20px; width: 334px; font-size: 15.5px; line-height: 20.5px; text-align: justify; }
  .message__terms { top: 114px; width: 372px; font-size: 15.5px; line-height: 20.5px; }
  .message__fine { top: 180px; width: 372px; font-size: 13.5px; line-height: 18.5px; text-align: justify; }
  .message__cta { top: 270px; font-weight: 700; font-size: 18.5px; line-height: 24px; }
  .message__email { top: 294px; font-size: 18.5px; line-height: 24px; }
  .call--back { left: 20px; top: 345px; }

  .stamp { position: absolute; left: 661px; top: 38px; width: 74px; height: 87px; background: var(--stamp); }
  .address-line { position: absolute; left: 481px; width: 251px; height: 1px; background: var(--rule); }
  .brand--back { left: 565px; top: 452px; font-size: 15px; line-height: 1.1; }
  .brand--back .brand__dot { width: 26px; height: 26px; }
</style>
</head>
<body>

<section class="card card--front">
  <div class="photo" role="img" aria-label="Photo of a smiling couple, woman hugging man from behind outdoors"></div>

  <h1 class="headline">Cash Out<br>Equita Loan</h1>
  <div class="subhead-bar">On your invesment property</div>

  <h2 class="benefits-title">LOAN BAND ON YOUR EQUITY</h2>
  <ul class="benefits">
    <li><svg viewBox="0 0 16 16"><path d="M1 9l4 4 10-11" fill="none" stroke="#0f3558" stroke-width="3"/></svg>Fast close</li>
    <li><svg viewBox="0 0 16 16"><path d="M1 9l4 4 10-11" fill="none" stroke="#0f3558" stroke-width="3"/></svg>No Income Qualifying</li>
    <li><svg viewBox="0 0 16 16"><path d="M1 9l4 4 10-11" fill="none" stroke="#0f3558" stroke-width="3"/></svg>Not based on credit scores</li>
    <li><svg viewBox="0 0 16 16"><path d="M1 9l4 4 10-11" fill="none" stroke="#0f3558" stroke-width="3"/></svg>competive Rater</li>
  </ul>

  <div class="brand brand--front"><span class="brand__dot"></span><span>Harbor Crest<br>Lending, Inc.</span></div>
  <div class="nmls">NMLS #481920</div>

  <svg class="call-band" viewBox="0 0 460 102" preserveAspectRatio="none">
    <defs>
      <linearGradient id="bandNavy" x1="0" x2="1">
        <stop offset="0" stop-color="#0b2a48"/><stop offset="1" stop-color="#164a73"/>
      </linearGradient>
    </defs>
    <path d="M0 0 H340 Q360 0 375 18 L438 102 H0 Z" fill="url(#bandNavy)"/>
    <path d="M340 0 Q360 0 375 18 L438 102 H446 L381 14 Q364 -2 340 0 Z" fill="#c98a3a"/>
  </svg>
  <div class="call call--front">
    <span class="call__icon"><svg viewBox="0 0 24 24"><path d="M7 2c1 0 2 3 2 4s-2 1.5-2 2.5 3 7 4 7 1.5-1.5 2.5-1.5 3 1.5 3 2.5-2 4-4 4C8 20.5 3 11 3 6c0-2 3-4 4-4z" fill="none" stroke="#0f3558" stroke-width="1.6"/></svg></span>
    <span>800-555-0147</span>
  </div>
</section>

<section class="card card--back">
  <svg class="back-shape" viewBox="0 0 766 520">
    <defs>
      <linearGradient id="discNavy" x1="0" y1="0" x2="1" y2="1">
        <stop offset="0" stop-color="#0b2a48"/><stop offset="1" stop-color="#17507c"/>
      </linearGradient>
      <linearGradient id="ribbonRed" x1="0" x2="1">
        <stop offset="0" stop-color="#c8141b"/><stop offset="1" stop-color="#e82a2f"/>
      </linearGradient>
    </defs>
    <circle cx="135" cy="174" r="312" fill="#c98a3a"/>
    <circle cx="135" cy="174" r="302" fill="#ffffff"/>
    <circle cx="135" cy="184" r="300" fill="#d3cfd2"/>
    <circle cx="135" cy="174" r="284" fill="url(#discNavy)"/>
    <polygon points="411,302 449,334 396,334" fill="#b0111a"/>
    <polygon points="0,334 449,334 399,420 0,420" fill="url(#ribbonRed)"/>
  </svg>

  <div class="message">
    <p class="message__intro">I am pleaved to in form you that an aquity baved lone is available for your invesment property.this no qulifying lone is posible simple due to the equlity you have.</p>
    <p class="message__terms">Loan is subject to confimotive of equlity and is for income property, invesment property, final property billness perpose other condition and property apply.</p>
    <p class="message__fine">Please call for compleate program requerments and details. harbor crest lending.Inc. 22-400 harbor road suite 210, bay city ca dept . of real eatotr corporate lic. #04572913, NMLS # 481920</p>
    <p class="message__cta">Please call for a quote</p>
    <p class="message__email">you can also email dan@hcl.loan</p>
  </div>

  <div class="call call--back">
    <span class="call__icon"><svg viewBox="0 0 24 24"><path d="M7 2c1 0 2 3 2 4s-2 1.5-2 2.5 3 7 4 7 1.5-1.5 2.5-1.5 3 1.5 3 2.5-2 4-4 4C8 20.5 3 11 3 6c0-2 3-4 4-4z" fill="none" stroke="#0f3558" stroke-width="1.6"/></svg></span>
    <span>800-555-0147</span>
  </div>

  <div class="stamp"></div>
  <div class="address-line" style="top:162px"></div>
  <div class="address-line" style="top:211px"></div>
  <div class="address-line" style="top:261px"></div>
  <div class="address-line" style="top:313px"></div>

  <div class="brand brand--back"><span class="brand__dot"></span><span>Harbor Crest<br>Lending, Inc.</span></div>
</section>

</body>
</html>
```